Business card for auto dealership

Looking for a clean modern design.
Would like attached logo incorporated

Industry/Entity Type

Car dealership

Contact Information for Business Card

Name, website, phone, cell, fax, email

```html
<!DOCTYPE html>
<html lang="en">
<head>
<meta charset="utf-8">
<title>Harlow Truck &amp; Auto Sales – Business Card</title>
<link href="https://fonts.googleapis.com/css2?family=Montserrat:wght@400;500&display=swap" rel="stylesheet">
<style>
  :root {
    --bg: #3a3a3a;
    --ink: #111111;
    --paper: #ffffff;
    --muted: #d9d9d9;
  }
  * { box-sizing: border-box; margin: 0; padding: 0; }
  html, body { width: 1200px; height: 1200px; overflow: hidden; }
  body {
    background: var(--bg);
    font-family: "Montserrat", sans-serif;
    display: flex;
    flex-direction: column;
    align-items: center;
    justify-content: center;
    gap: 60px;
  }
  .card {
    position: relative;
    width: 840px;
    height: 480px;
    border-radius: 34px;
    overflow: hidden;
    background: var(--ink);
  }
  /* Front */
  .card-front .top-panel {
    position: absolute;
    left: 0; top: 0; right: 0;
    height: 268px;
    background: var(--paper);
    display: flex;
    align-items: center;
    justify-content: center;
  }
  .card-front .divider {
    position: absolute;
    left: 0; right: 0;
    top: 276px;
    height: 10px;
    background: var(--paper);
  }
  .wordmark {
    font-weight: 500;
    text-align: center;
    line-height: 1.1;
    letter-spacing: 0.04em;
  }
  .wordmark .name-line { display: block; font-size: 88px; }
  .wordmark .sub-line { display: block; font-size: 24px; letter-spacing: 0.12em; }
  .card-front .wordmark { color: var(--ink); }
  .holder {
    position: absolute;
    left: 60px;
    top: 350px;
    padding-left: 18px;
    border-left: 5px solid var(--paper);
    color: var(--paper);
  }
  .holder .holder-name { font-size: 30px; font-weight: 500; letter-spacing: 0.03em; }
  .holder .holder-role { font-size: 15px; font-weight: 400; color: var(--muted); letter-spacing: 0.04em; margin-top: 2px; }
  .contact-list {
    position: absolute;
    left: 470px;
    top: 310px;
    list-style: none;
    color: var(--paper);
    font-size: 20px;
  }
  .contact-list li { display: flex; align-items: center; gap: 12px; height: 33px; }
  .contact-list svg { width: 22px; height: 22px; fill: var(--paper); flex: none; }
  /* Back */
  .card-back { display: flex; flex-direction: column; align-items: center; justify-content: center; }
  .card-back .wordmark { color: var(--paper); }
  .card-back .site {
    position: absolute;
    bottom: 48px;
    left: 0; right: 0;
    text-align: center;
    color: var(--muted);
    font-size: 26px;
    letter-spacing: 0.06em;
  }
</style>
</head>
<body>
  <section class="card card-front">
    <div class="top-panel">
      <p class="wordmark"><span class="name-line">Harlow</span><span class="sub-line">TRUCK &amp; AUTO SALES</span></p>
    </div>
    <div class="divider"></div>
    <div class="holder">
      <p class="holder-name">CASEY HARLOW</p>
      <p class="holder-role">POSITION</p>
    </div>
    <ul class="contact-list">
      <li>
        <svg viewBox="0 0 24 24" aria-hidden="true"><path d="M6.6 10.8a15 15 0 0 0 6.6 6.6l2.2-2.2c.3-.3.7-.4 1-.2 1.1.4 2.3.6 3.6.6.6 0 1 .4 1 1V20c0 .6-.4 1-1 1A17 17 0 0 1 3 4c0-.6.4-1 1-1h3.5c.6 0 1 .4 1 1 0 1.3.2 2.5.6 3.6.1.3 0 .7-.2 1z"/></svg>
        555-210-4830
      </li>
      <li>
        <svg viewBox="0 0 24 24" aria-hidden="true"><path d="M7 1h10a2 2 0 0 1 2 2v18a2 2 0 0 1-2 2H7a2 2 0 0 1-2-2V3a2 2 0 0 1 2-2zm0 3v14h10V4zm5 15.5a1 1 0 1 0 0 2 1 1 0 0 0 0-2z"/></svg>
        555-367-9152
      </li>
      <li>
        <svg viewBox="0 0 24 24" aria-hidden="true"><path d="M6 2h9l3 3v5h1a2 2 0 0 1 2 2v8a2 2 0 0 1-2 2H5a2 2 0 0 1-2-2v-8a2 2 0 0 1 2-2h1zm2 2v6h8V6h-2V4zm-1 9v2h2v-2zm4 0v2h2v-2zm4 0v2h2v-2zm-8 3v2h2v-2zm4 0v2h2v-2zm4 0v2h2v-2z"/></svg>
        555-604-2718
      </li>
      <li>
        <svg viewBox="0 0 24 24" aria-hidden="true"><path d="M2 5h20v14H2zm2 2v.5l8 5.5 8-5.5V7zm0 2.9V17h16V9.9l-8 5.5z"/></svg>
        casey@harlowauto.com
      </li>
    </ul>
  </section>

  <section class="card card-back">
    <p class="wordmark"><span class="name-line">Harlow</span><span class="sub-line">TRUCK &amp; AUTO SALES</span></p>
    <p class="site">HARLOWAUTO.COM</p>
  </section>
</body>
</html>
```